Criação de Kit Layout de Posts para Redes Sociais (Facebook, Instagram e etc) para Advocacia e Direito
" Prestamos assessoria para os clientes saberem sua situação atual, perante a Previdência Social, e fazemos um planejamento previdenciário, com acompanhamento até a concessão do benefício pretendido, seja pela via administrativa, seja pela via judicial. Assim, realizamos contagem de tempo de contribuição, simulação de valor de benefício, planejamento previdenciário, requerimento administrativo e ajuizamento de ação judicial, tudo para o fim de obter a concessão de Aposentadoria, revisão de benefício, Auxílio-Doença, Auxílio-Acidente, Salário-Maternidade, Pensão por morte, Auxílio-Reclusão e Benefício Assistencial. "

```html
<!DOCTYPE html>
<html lang="pt-BR">
<head>
<meta charset="UTF-8">
<title>Aposentadoria por Idade — Post</title>
<link href="https://fonts.googleapis.com/css2?family=Montserrat:wght@500;600;700&display=swap" rel="stylesheet">
<style>
  :root {
    --navy: #112244;
    --navy-deep: #0b1a36;
    --gold: #c9a66b;
    --gold-soft: #d9c29a;
    --cream: #f4efe6;
    --photo-light: #dfe4ea;
    --photo-mid: #b9c3cf;
    --photo-dark: #7d8a9c;
    --headline: #1b2f57;
  }
  * { margin: 0; padding: 0; box-sizing: border-box; }
  html, body { width: 1200px; height: 1200px; overflow: hidden; background: var(--cream); }
  .post {
    position: relative;
    width: 1200px;
    height: 1200px;
    overflow: hidden;
    font-family: "Montserrat", sans-serif;
    background: linear-gradient(90deg, var(--gold-soft) 0%, var(--cream) 40%, #ffffff 100%);
  }
  .scene-photo {
    position: absolute;
    left: 0; top: 283px;
    width: 1200px; height: 917px;
    background:
      radial-gradient(ellipse 420px 600px at 880px 620px, rgba(120,130,150,0.35), transparent 70%),
      linear-gradient(90deg, rgba(201,166,107,0.75) 0%, rgba(214,196,160,0.45) 22%, rgba(223,228,234,0.2) 45%, rgba(185,195,207,0.3) 100%),
      linear-gradient(180deg, var(--photo-mid) 0%, var(--photo-light) 45%, var(--photo-mid) 100%);
  }
  .scene-photo::after {
    content: "";
    position: absolute;
    left: 0; top: 0; width: 100%; height: 100%;
    background: radial-gradient(ellipse 520px 160px at 680px 470px, rgba(255,255,255,0.55), transparent 75%);
  }
  .top-band {
    position: absolute;
    left: 0; top: 101px;
    width: 1200px; height: 182px;
    background: linear-gradient(90deg, var(--navy-deep) 0%, var(--navy) 60%, #1a2d52 100%);
  }
  .brand-box {
    position: absolute;
    left: 84px; top: 34px;
    width: 389px; height: 384px;
    background: linear-gradient(160deg, #16294d 0%, var(--navy-deep) 100%);
    border: 4px solid var(--gold);
    display: flex;
    align-items: center;
    justify-content: center;
    gap: 18px;
  }
  .brand-mark {
    width: 26px; height: 26px;
    background: var(--gold);
    flex: none;
  }
  .brand-name {
    color: #ffffff;
    font-weight: 600;
    font-size: 30px;
    line-height: 1.15;
    letter-spacing: 1px;
  }
  .headline {
    position: absolute;
    left: 290px; top: 700px;
    width: 810px;
    text-align: center;
    color: var(--headline);
  }
  .headline-title {
    font-weight: 700;
    font-size: 42px;
    line-height: 1.2;
  }
  .headline-sub {
    font-weight: 600;
    font-size: 33px;
    line-height: 1.35;
    margin-top: 6px;
  }
</style>
</head>
<body>
  <main class="post">
    <div class="scene-photo" role="img" aria-label="Photo of a bearded professional in a beige suit and yellow hard hat holding a tablet inside a warehouse with tall shelving"></div>
    <div class="top-band"></div>
    <div class="brand-box">
      <span class="brand-mark"></span>
      <span class="brand-name">VALADARES<br>MOREIRA</span>
    </div>
    <div class="headline">
      <h1 class="headline-title">Aposentadoria por Idade:</h1>
      <p class="headline-sub">como funciona? Como pode ficar após a reforma?</p>
    </div>
  </main>
</body>
</html>
```